Lumorax Helpdesk overview brochure

Take the word document that is attached and turn it into a brochure. (Thinking one page, front and back.) the only existing branding/colors we have is the logo that is on the document. It may require a phone all or a bit of back and forth in text to explain some of the concepts in the attached document.

Target Market(s)

Call centers

Industry/Entity Type

It Service

Font styles to use
Sans Serif

Colors

Designer to choose colors to be used in the design.

Requirements
Must have
• A crisp professional look

```html
<!DOCTYPE html>
<html lang="en">
<head>
<meta charset="utf-8">
<title>Lumorax Helpdesk overview brochure</title>
<link href="https://fonts.googleapis.com/css2?family=Cinzel:wght@400;600&family=Roboto+Condensed:wght@400;500&family=Roboto:wght@400;500&display=swap" rel="stylesheet">
<style>
:root{
  --stage:#5a4636;
  --paper:#ffffff;
  --ink:#222629;
  --muted:#4a4f54;
  --blue:#1e8fd6;
  --blue-dark:#0f5f98;
  --sky-top:#4f8fc2;
  --sky-bottom:#d7e7f3;
  --tech-top:#0a2f48;
  --tech-bottom:#2a86b8;
  --panel:#ececec;
  --footer:#eef0f2;
}
*{margin:0;padding:0;box-sizing:border-box}
html,body{width:1200px;height:800px;overflow:hidden}
body{background:var(--stage);position:relative;font-family:"Roboto Condensed",Arial,sans-serif;color:var(--ink)}
.page{position:absolute;top:10px;width:560px;height:780px;background:var(--paper);overflow:hidden;box-shadow:0 4px 14px rgba(0,0,0,.45)}
.page--front{left:30px}
.page--back{left:610px}
.abs{position:absolute}

/* front */
.hero-photo{left:0;top:0;width:560px;height:450px;background:linear-gradient(160deg,var(--sky-top),#7fb2d8 55%,var(--sky-bottom))}
.swoosh{left:0;width:560px}
.title{left:0;width:560px;top:478px;text-align:center;font-family:"Cinzel",Georgia,serif;font-size:36px;font-weight:600;letter-spacing:1px;color:#1b1b1b}
.tagline{left:0;width:560px;top:524px;text-align:center;font-family:"Cinzel",Georgia,serif;font-size:11.5px;line-height:15px;color:var(--blue)}
.intro-col{top:570px;font-size:8.4px;line-height:10.2px;color:var(--muted);text-align:justify}
.intro-col--left{left:0;width:282px;height:130px;background:var(--panel);padding:12px 14px 0 18px}
.intro-col--right{left:290px;width:252px;padding-top:12px}
.intro-col p{border-left:2px solid var(--blue);padding-left:8px;margin-bottom:10px}
.intro-col p::first-letter{font-size:11px}

/* footer */
.footer{left:0;top:690px;width:560px;height:90px;background:var(--footer)}
.brand{left:28px;top:20px;display:flex;align-items:center;gap:10px}
.brand-dot{width:40px;height:40px;border-radius:50%;background:var(--blue)}
.brand-name{font-family:"Cinzel",Georgia,serif;font-size:19px;line-height:20px;color:var(--blue);font-weight:400}
.contact{left:320px;top:14px;font-size:11px}
.contact h3{font-family:"Roboto Condensed",Arial,sans-serif;font-weight:500;font-size:13px;color:var(--ink);margin-bottom:6px}
.contact-row{display:flex;align-items:center;gap:5px;font-size:10.5px;margin-bottom:5px}
.contact-row small{font-size:7.5px}
.contact-row svg{flex:none}
.contact-web{margin-left:18px;font-size:7.5px}

/* back */
.tech-photo{left:0;top:0;width:560px;height:210px;background:linear-gradient(135deg,var(--tech-top),#135a82 55%,var(--tech-bottom))}
.costs-head{left:22px;top:242px;font-size:11px;color:var(--blue);font-weight:500}
.cost{top:268px;display:flex;align-items:center;gap:8px;font-size:7.6px;line-height:11px}
.cost b{font-size:10.5px;font-weight:500}
.cost-icon{width:26px;height:26px;border-radius:50%;background:#3b3f44;display:flex;align-items:center;justify-content:center}
.footnote{right:22px;top:310px;font-size:6.8px;color:var(--blue)}
.channel-band{left:20px;top:328px;width:520px;height:90px}
.channel{position:absolute;width:52px;height:52px;border-radius:50%;background:#fff;display:flex;align-items:center;justify-content:center;text-align:center;font-size:7.5px;line-height:9px;color:var(--blue-dark);font-weight:500}
.lead{left:22px;top:432px;font-size:7.8px;color:var(--ink)}
.model-head{left:22px;top:456px;font-family:"Cinzel",Georgia,serif;font-size:12px;color:var(--blue-dark);letter-spacing:.5px}
.sub-head{font-size:10px;text-decoration:underline;color:var(--ink);font-weight:500}
.proposal{left:22px;top:473px}
.proposal p{font-size:7.8px;margin-top:4px;color:var(--muted)}
.plan-col{top:516px;font-size:7.6px;color:var(--muted)}
.plan-col--left{left:22px;width:245px}
.plan-col--right{left:282px;width:250px}
.plan-col > p{margin:5px 0 6px;line-height:9.5px}
.checklist{list-style:none}
.checklist li{position:relative;padding-left:14px;margin-bottom:5.5px;line-height:9px}
.checklist li::before{content:"";position:absolute;left:0;top:0;width:8px;height:8px;border:1.6px solid var(--blue);border-radius:50% 50% 50% 0}
</style>
</head>
<body>

<section class="page page--front">
  <div class="abs hero-photo" role="img" aria-label="Contact centre agent wearing a headset beside a glowing world map and sound wave"></div>
  <svg class="abs swoosh" style="top:380px" width="560" height="100" viewBox="0 0 560 100">
    <path d="M0 40 C150 90 380 95 560 60 L560 100 L0 100 Z" fill="#1e8fd6"/>
    <path d="M0 62 C150 108 380 108 560 76 L560 100 L0 100 Z" fill="#ffffff"/>
  </svg>
  <h1 class="abs title">LUMORAX HELPDESK</h1>
  <p class="abs tagline">HELPS CONTACT CENTERS SERVE NEW CUSTOMER ACCESS CHANNELS,<br>IMPROVE CUSTOMER SERVICE, AND LOWER COSTS OF OPERATION</p>
  <div class="abs intro-col intro-col--left">
    <p>The huge popularity of social media and messaging is creating customer preferences to communicate with your company using SMS text messaging, Chatterly, Teamloop, Voxi, Orbi Assistant, Nestra Home, and many other new channels.</p>
    <p>App fatigue has set in. Customers are weary of installing, updating and learning how to use mobile apps. Your customers want to communicate with you using their messaging service of choice or just talk into their smart phone, computer, Orbi Assistant or similar device.</p>
  </div>
  <div class="abs intro-col intro-col--right">
    <p>Sensible automation of customer interactions on these new channels can provide better service at even lower costs of operation.</p>
    <p>According to Veltrane's report, by 2020, 85% of customer interactions will be managed without a human.</p>
    <p>Using specific techniques, Lumorax Helpdesk will help you shift some traffic from higher cost telephone calls to lower cost messaging channels. Shaping your traffic into lower cost channels has</p>
  </div>
  <footer class="abs footer">
    <div class="abs brand"><span class="brand-dot"></span><span class="brand-name">LUMORAX<br>HELPDESK</span></div>
    <div class="abs contact">
      <h3>CONTACT INFORMATION IS:</h3>
      <div class="contact-row">
        <svg width="12" height="10" viewBox="0 0 12 10"><path d="M1 3 Q6 -1 11 3 L9 5 L7.5 3.5 L4.5 3.5 L3 5 Z M3 5 L9 5 L10 9 L2 9 Z" fill="#1e8fd6"/></svg>
        555-204-7381
        <svg class="contact-web" width="10" height="10" viewBox="0 0 10 10"><circle cx="5" cy="5" r="4.3" fill="none" stroke="#1e8fd6"/><path d="M0.7 5H9.3M5 0.7V9.3M2.3 2.5H7.7M2.3 7.5H7.7" stroke="#1e8fd6" stroke-width=".7"/></svg>
        <small>www.lumoraxsolutions.net</small>
      </div>
      <div class="contact-row">
        <svg width="10" height="12" viewBox="0 0 10 12"><path d="M5 12 C1 7 1 5.5 1 4.5 A4 4 0 0 1 9 4.5 C9 5.5 9 7 5 12 Z" fill="#1e8fd6"/><circle cx="5" cy="4.5" r="1.5" fill="#fff"/></svg>
        <small>4120 W. Harlow Avenue • Suite B Brenton, IL 60999</small>
      </div>
    </div>
  </footer>
</section>

<section class="page page--back">
  <div class="abs tech-photo" role="img" aria-label="Hand touching glowing phone, email and at-sign icons over a circuit pattern"></div>
  <svg class="abs swoosh" style="top:150px" width="560" height="90" viewBox="0 0 560 90">
    <path d="M0 30 C170 75 400 78 560 30 L560 90 L0 90 Z" fill="#1e8fd6"/>
    <path d="M0 48 C170 92 400 92 560 48 L560 90 L0 90 Z" fill="#ffffff"/>
  </svg>
  <h2 class="abs costs-head">EXISTING CHANNELS HAVE DIFFERENT COSTS:</h2>
  <div class="abs cost" style="left:22px">
    <span class="cost-icon"><svg width="14" height="14" viewBox="0 0 14 14"><circle cx="7" cy="4.5" r="3" fill="#fff"/><path d="M1.5 14 C1.5 9 12.5 9 12.5 14 Z" fill="#fff"/></svg></span>
    <span>Telephone call with a live agent<br>Average cost per call is <b>$17</b> *</span>
  </div>
  <div class="abs cost" style="left:206px">
    <span class="cost-icon"><svg width="14" height="10" viewBox="0 0 14 10"><rect x=".5" y=".5" width="13" height="9" fill="none" stroke="#fff"/><path d="M.5 .5 L7 6 L13.5 .5" fill="none" stroke="#fff"/></svg></span>
    <span>Email with a live agent<br>Average cost per email is <b>$15</b>*</span>
  </div>
  <div class="abs cost" style="left:390px">
    <span class="cost-icon"><svg width="14" height="13" viewBox="0 0 14 13"><ellipse cx="7" cy="5.5" rx="6" ry="4.5" fill="none" stroke="#fff" stroke-width="1.3"/><path d="M3 9 L2 12.5 L6 10" fill="#fff"/></svg></span>
    <span>Telephone call with a live agent<br>Average cost per call is <b>$17</b> *</span>
  </div>
  <p class="abs footnote">*Above costs are sited from an Corvale research paper</p>
  <div class="abs channel-band">
    <svg class="abs" style="left:0;top:0" width="520" height="90" viewBox="0 0 520 90">
      <path d="M0 8 C120 -6 200 22 300 14 C400 6 460 -4 520 4 L520 86 C420 76 300 96 180 84 C100 76 40 92 0 84 Z" fill="#1e8fd6"/>
    </svg>
    <div class="channel" style="left:16px;top:20px">SMS</div>
    <div class="channel" style="left:106px;top:8px">Team-<br>loop</div>
    <div class="channel" style="left:196px;top:6px">Orbi</div>
    <div class="channel" style="left:286px;top:12px">Kipchat</div>
    <div class="channel" style="left:376px;top:24px">Nestra<br>Home</div>
    <div class="channel" style="left:456px;top:12px">Wave-<br>talk</div>
  </div>
  <p class="abs lead">With these new channels, the cost is similar to webchat. Carefully automated interactions are at an even lower cost</p>
  <h2 class="abs model-head">ENGAGEMENT MODEL</h2>
  <div class="abs proposal">
    <h3 class="sub-head" style="margin-top:12px">PROPOSAL</h3>
    <p>Lumorax Helpdesk provides a written proposal. The proposal will describe our engagement methodologies and costs.</p>
  </div>
  <div class="abs plan-col plan-col--left">
    <h3 class="sub-head">ENGAGEMENT</h3>
    <p>Lumorax Helpdesk will meet with all the relevant stake holders on site and gather information to identify:</p>
    <ul class="checklist">
      <li>Historical traffic patterns.</li>
      <li>Actual costs by channel</li>
      <li>Review marketing plans that may impact customer service</li>
      <li>Review product plans that may impact customer service.</li>
      <li>Explore competition landscape as it relates to customer service.</li>
      <li>Review the existing corporate data store, analytics and reporting</li>
      <li>Review the current plans, metrics and budgets for customer service support</li>
    </ul>
  </div>
  <div class="abs plan-col plan-col--right">
    <h3 class="sub-head">TRANSFORMATION REPORT</h3>
    <ul class="checklist" style="margin-top:7px">
      <li>Executive summary</li>
      <li>Cost analysis per contact by channel</li>
      <li>Traffic patterns by channel</li>
      <li>Probable impacts of product and marketing plans</li>
      <li>Recommendations for achieving competitive advantage through service</li>
      <li>Recommendations for new channel types</li>
      <li>Recommendations for traffic shaping</li>
      <li>Near and long-term options for sensible automation</li>
      <li>Technology recommendations for implementing new channels</li>
      <li>Projected financial impact of recommendations</li>
    </ul>
  </div>
  <footer class="abs footer">
    <div class="abs brand"><span class="brand-dot"></span><span class="brand-name">LUMORAX<br>HELPDESK</span></div>
    <div class="abs contact">
      <h3>CONTACT INFORMATION IS:</h3>
      <div class="contact-row">
        <svg width="12" height="10" viewBox="0 0 12 10"><path d="M1 3 Q6 -1 11 3 L9 5 L7.5 3.5 L4.5 3.5 L3 5 Z M3 5 L9 5 L10 9 L2 9 Z" fill="#1e8fd6"/></svg>
        555-204-7381
        <svg class="contact-web" width="10" height="10" viewBox="0 0 10 10"><circle cx="5" cy="5" r="4.3" fill="none" stroke="#1e8fd6"/><path d="M0.7 5H9.3M5 0.7V9.3M2.3 2.5H7.7M2.3 7.5H7.7" stroke="#1e8fd6" stroke-width=".7"/></svg>
        <small>www.lumoraxsolutions.net</small>
      </div>
      <div class="contact-row">
        <svg width="10" height="12" viewBox="0 0 10 12"><path d="M5 12 C1 7 1 5.5 1 4.5 A4 4 0 0 1 9 4.5 C9 5.5 9 7 5 12 Z" fill="#1e8fd6"/><circle cx="5" cy="4.5" r="1.5" fill="#fff"/></svg>
        <small>4120 W. Harlow Avenue • Suite B Brenton, IL 60999</small>
      </div>
    </div>
  </footer>
</section>

</body>
</html>
```